Riverbend Haven Home Care-Nursing Assessment Form

I am creating a Nursing Assessment Form (which is used to be an intake form for all new patients) for my new home care company, Riverbend Haven Home Care.

It is 15 pages and pretty comprehensive as this is a very regulated field. I have all the necessary content and information attached in the word document below. Now, I am seeking a designer to make it look professional, cohesive and easy to read/ follow.
In order for your Word Document Design to be selected, you must:

1. As mentioned previously, make it easy to read/follow. There should be enough spacing, room to write out all necessary notes, fill out check marks...etc...
2. It should look professional.
3. It should be attractive and eye pleasing. Attached you will find our logo-kindly incorporate it's style into the project as well. The logo should be placed on top of each page.
4. Lastly, we need a Word Document version AND PDF Fillable Option. The fillable PDF should Auto Fill for the Name and Start of Care (SOC) Date.

I have attached a sample form below as well. This is how I envision the finished project to look. Of course, I am open to other suggestions as look as it meets the aforementioned requirements.

Thank you! May the best man or woman win!
Our team looks forward to working with our designer on this project!

Industry/Entity Type

Home Health Care

Font styles to use
Sans Serif

Colors
0255a3
9bcb3c

Requirements
Must have
• Refer to Project Description above.
Nice to have
We must be given a Word Document Option and PDF Fillable Option.

```html
<!DOCTYPE html>
<html lang="en">
<head>
<meta charset="utf-8">
<title>Riverbend Haven Home Care – Initial Assessment Form</title>
<link href="https://fonts.googleapis.com/css2?family=PT+Sans:wght@400;700&display=swap" rel="stylesheet">
<style>
  :root {
    --backdrop: #5f7690;
    --paper: #f7f7f7;
    --brand-blue: #0255a3;
    --navy: #1b3f7a;
    --brand-green: #9bcb3c;
    --green-dark: #6cab1f;
    --header-green: #c4dd97;
    --header-green-light: #e4efcf;
    --row-alt: #eeeeee;
    --ink: #2a2a2a;
    --rule: #4a6fa5;
  }
  * { box-sizing: border-box; margin: 0; padding: 0; }
  html, body { width: 1200px; height: 1000px; overflow: hidden; }
  body {
    background: var(--backdrop);
    font-family: "PT Sans", sans-serif;
    color: var(--ink);
    position: relative;
  }
  .form-page {
    position: absolute; left: 288px; top: 97px;
    width: 623px; height: 806px;
    background: var(--paper);
  }
  .form-page > * { position: absolute; }

  .brand { left: 37px; top: 36px; display: flex; align-items: center; gap: 10px; }
  .brand-dot { width: 40px; height: 40px; border-radius: 50%; background: var(--brand-blue); }
  .brand-name { font-size: 17px; font-weight: 700; color: var(--brand-blue); line-height: 1.1; width: 200px; }

  .fill-field { display: flex; align-items: flex-end; font-size: 10px; font-weight: 700; color: var(--navy); }
  .fill-field .line { flex: 1; border-bottom: 1px solid var(--rule); margin-left: 4px; height: 10px; }
  .field-name { left: 352px; top: 38px; width: 236px; }
  .field-soc { left: 352px; top: 56px; width: 236px; }

  .form-title { left: 37px; top: 96px; width: 550px; display: flex; align-items: center; gap: 6px;
    font-size: 16px; font-weight: 400; color: var(--navy); white-space: nowrap; }
  .form-title .double-rule { flex: 1; height: 5px; border-top: 1.5px solid var(--rule); border-bottom: 1.5px solid var(--rule); }
  .section-title { left: 37px; top: 127px; width: 550px; display: flex; align-items: center; gap: 14px;
    font-size: 11px; font-weight: 700; color: var(--navy); white-space: nowrap; }
  .section-title .single-rule { flex: 1; border-top: 1.5px solid var(--rule); }

  .field-patient { left: 37px; top: 154px; width: 290px; font-size: 8px; }
  .intro { left: 37px; top: 181px; font-size: 8.5px; }

  .checklist { left: 37px; top: 200px; width: 550px; border-collapse: collapse; border: 1px solid #555; font-size: 8.5px; }
  .checklist th { height: 20px; font-weight: 400; text-align: center; background: var(--header-green-light); border-left: 1px solid #555; border-bottom: 1px solid #555; }
  .checklist th.topic { text-align: left; padding-left: 6px; background: var(--header-green); border-left: none; }
  .checklist th.col-no { background: var(--header-green); }
  .checklist td { height: 20.8px; border-left: 1px solid #555; text-align: center; vertical-align: middle; }
  .checklist td.topic { border-left: none; text-align: left; padding-left: 12px; }
  .checklist td.topic span { display: inline-block; width: 16px; text-align: right; margin-right: 8px; }
  .checklist tr:nth-child(even) td { background: var(--row-alt); }
  .checklist tr.tall td { height: 32px; line-height: 1.25; }
  .checklist tr.tall td.topic { padding-left: 36px; text-indent: -24px; }
  .box { display: inline-block; width: 8px; height: 8px; border: 1px solid var(--brand-green); vertical-align: middle; }

  .question { left: 37px; font-size: 8px; letter-spacing: .2px; display: flex; gap: 10px; align-items: center; }
  .question .opt { color: var(--green-dark); font-weight: 700; }
  .question .opt .box { margin-right: 4px; }
  .question .opt.muted { color: #666; font-weight: 400; }
  .question .send-line { display: inline-block; width: 110px; border-bottom: 1px solid #888; height: 8px; }

  .consent { left: 37px; top: 534px; width: 550px; font-size: 9.3px; line-height: 12.3px; }
  .field-row { left: 37px; width: 550px; font-size: 8px; font-weight: 400; color: var(--ink); }
  .field-row .line { border-color: #444; }
  .release { left: 37px; top: 656px; width: 550px; font-size: 9.5px; line-height: 13px; font-weight: 700; color: var(--navy); }
  .confirm { left: 37px; top: 690px; font-size: 8px; color: var(--navy); font-weight: 700; }
  .signatures { left: 37px; top: 722px; width: 550px; display: flex; gap: 8px; }
  .signatures .fill-field { color: var(--navy); font-weight: 400; font-size: 8px; }

  .footer-rule { top: 768px; border-top: 1.5px solid var(--rule); width: 245px; }
  .footer-rule.left { left: 37px; }
  .footer-rule.right { left: 343px; }
  .footer-dot { left: 298px; top: 752px; width: 32px; height: 32px; border-radius: 50%; background: var(--brand-blue); }
  .page-number { left: 575px; top: 776px; font-size: 9px; font-weight: 700; color: var(--navy); }
</style>
</head>
<body>
<main class="form-page">
  <div class="brand"><div class="brand-dot"></div><div class="brand-name">Riverbend Haven Home Care</div></div>
  <div class="fill-field field-name">Name:<span class="line"></span></div>
  <div class="fill-field field-soc">SOC Date:<span class="line"></span></div>

  <h1 class="form-title">Initial Assessment Form <span class="double-rule"></span></h1>
  <h2 class="section-title">Start of Care Checklist, Patient Consent and Authorization <span class="single-rule"></span></h2>

  <div class="fill-field field-patient">Patient's Name:<span class="line"></span></div>
  <p class="intro">During the patient/family interview and assessment, the following were discussed and provided:</p>

  <table class="checklist">
    <colgroup><col style="width:379px"><col style="width:56px"><col style="width:58px"><col style="width:57px"></colgroup>
    <tr><th class="topic">DISCUSSED &amp; PROVIDED</th><th>YES</th><th class="col-no">NO</th><th>N/A</th></tr>
    <tr><td class="topic"><span>1.</span>Patient Information Booklet with Agency Information</td><td><i class="box"></i></td><td><i class="box"></i></td><td><i class="box"></i></td></tr>
    <tr><td class="topic"><span>2.</span>HIPAA Notice of Privacy Practices Booklet with Consent Form</td><td><i class="box"></i></td><td><i class="box"></i></td><td><i class="box"></i></td></tr>
    <tr><td class="topic"><span>3.</span>Advance Directive and Palliative Care Information</td><td><i class="box"></i></td><td><i class="box"></i></td><td><i class="box"></i></td></tr>
    <tr><td class="topic"><span>4.</span>Home Care Program, Contact Person, Telephone Numbers, and Payment</td><td><i class="box"></i></td><td><i class="box"></i></td><td><i class="box"></i></td></tr>
    <tr><td class="topic"><span>5.</span>Patient Bill of Rights &amp; Responsibilities</td><td><i class="box"></i></td><td><i class="box"></i></td><td><i class="box"></i></td></tr>
    <tr class="tall"><td class="topic"><span>6.</span>Plan of Care - services to be provided including plan of care developed with patient/family input and preferences when possible.</td><td><i class="box"></i></td><td><i class="box"></i></td><td><i class="box"></i></td></tr>
    <tr><td class="topic"><span>7.</span>Two Page Service Agreement</td><td><i class="box"></i></td><td><i class="box"></i></td><td><i class="box"></i></td></tr>
    <tr><td class="topic"><span>8.</span>Discharge Plan</td><td><i class="box"></i></td><td><i class="box"></i></td><td><i class="box"></i></td></tr>
    <tr><td class="topic"><span>9.</span>Grievance/Complaint Procedure</td><td><i class="box"></i></td><td><i class="box"></i></td><td><i class="box"></i></td></tr>
    <tr><td class="topic"><span>10.</span>Emergency Disaster Plan</td><td><i class="box"></i></td><td><i class="box"></i></td><td><i class="box"></i></td></tr>
  </table>

  <div class="question" style="top:456px">DOES THIS PATIENT HAVE AN ADVANCE DIRECTIVE? <span class="opt"><i class="box"></i>YES</span><span class="opt"><i class="box"></i>NO</span></div>
  <div class="question" style="top:474px">DOES THIS PATIENT HAVE A HEALTH CARE PROXY? <span class="opt"><i class="box"></i>YES</span><span class="opt"><i class="box"></i>NO</span></div>
  <div class="question" style="top:492px">DOES THIS PATIENT HAVE A DNR? <span class="opt"><i class="box"></i>YES</span><span class="opt"><i class="box"></i>NO</span></div>
  <div class="question" style="top:510px">COPY FOR RHHC OBTAINED: <span class="opt"><i class="box"></i>YES</span><span class="opt"><i class="box"></i>NO</span><span class="opt muted"><i class="box"></i>PATIENT/FAMILY TO SEND: <span class="send-line"></span></span></div>

  <p class="consent">I hereby give my consent to the company's personnel to perform all necessary procedures and treatments as indicated by my physician and indicated on my Plan of Care. Unless specified, I authorize and give my permission to release medical information to all members of my health care team needed for the provision of services, operations of Riverbend Haven, and also to any third party responsible for reimbursement. Permission is given to Riverbend Haven Home Care to give access and review of my clinical record information and home visit by surveyors/personnel representing regulatory bodies and/ or accrediting bodies for purposes of review or audit.</p>

  <div class="fill-field field-row" style="top:614px">INFORMATION MAY NOT BE RELEASED CONCERNING:<span class="line"></span></div>
  <div class="fill-field field-row" style="top:631px">INFORMATION MAY NOT BE RELEASED TO:<span class="line"></span></div>

  <p class="release">I acknowledge that I release the company and its employees from any liability claims related to the use of my vehicle or the employee's vehicle during the hours that services are being provided.</p>

  <p class="confirm">AS INDICATED, THE ABOVE INFORMATION WAS DISCUSSED AND PROVIDED TO ME.</p>
  <div class="fill-field field-row" style="top:704px;color:var(--navy)">PATIENT/AUTHORIZED REPRESENTATIVE SIGNATURE:<span class="line"></span></div>
  <div class="signatures">
    <div class="fill-field" style="width:370px">RN/WITNESS SIGNATURE:<span class="line"></span></div>
    <div class="fill-field" style="flex:1">DATE:<span class="line"></span></div>
  </div>

  <span class="footer-rule left"></span>
  <span class="footer-dot"></span>
  <span class="footer-rule right"></span>
  <span class="page-number">21</span>
</main>
</body>
</html>
```